Gentleman's grooming products require a business card

I need a business card that incorporates the logo [ or parts of ] that we had Art Parade design for us as uploaded.

We sell online, mens grooming products including moustache waxes, beard oils and shaving accessories.
We want a card that is classy, professional and a card that shouts mens products.

Target Market(s)

Young professional male market

Industry/Entity Type

Business

Contact Information for Business Card

Tess and Dulcie Abbott
Brass and Bristle
Purveyors of gentlemen's waxes, oils and grooming requisites
M :0491527306
E : tess@brassandbristle.com.au
E : dulcie@brassandbristle.com.au
E : sales@theboulevardpomade.com.au

W : www.brassandbristle.com.au

Requirements
Must have
• Class
Nice to have
• Professionalism

```html
<!DOCTYPE html>
<html lang="en">
<head>
<meta charset="utf-8">
<title>Brass and Bristle – Business Card</title>
<link rel="stylesheet" href="https://fonts.googleapis.com/css2?family=Open+Sans:wght@400;600;700&display=swap">
<style>
  :root {
    --backdrop: #e9e6e1;
    --card: #0b0b0b;
    --ink: #ffffff;
    --ink-soft: #d9d9d9;
    --rule: #bdbdbd;
    --art-dark: #1c1c1c;
    --art-mid: #3a3a3a;
    --band: #ffffff;
  }
  * { margin: 0; padding: 0; box-sizing: border-box; }
  html, body {
    width: 1200px; height: 950px; overflow: hidden;
    background: var(--backdrop);
    font-family: "Open Sans", Arial, sans-serif;
  }
  .canvas { position: relative; width: 1200px; height: 950px; }

  .card {
    position: absolute; top: 197px;
    width: 360px; height: 556px;
    background: var(--card); color: var(--ink);
    overflow: hidden;
    box-shadow: 0 10px 28px rgba(0,0,0,.25);
  }
  .card--front { left: 190px; }
  .card--back  { left: 650px; }

  /* brand block */
  .brand { position: absolute; left: 0; right: 0; text-align: center; }
  .brand__mark {
    display: block; width: 34px; height: 34px; margin: 0 auto 8px;
    border: 1.5px solid var(--ink);
  }
  .brand__name {
    font-weight: 600; font-size: 30px; letter-spacing: .5px; line-height: 1;
    color: var(--ink);
  }
  .brand__rule { height: 1px; background: var(--rule); margin: 8px 22px 4px; }
  .brand__tagline {
    font-size: 6.5px; letter-spacing: .9px; text-transform: uppercase;
    color: var(--ink-soft);
  }
  .card--front .brand { top: 30px; }

  /* contact block */
  .contact { position: absolute; left: 40px; right: 40px; top: 168px; text-align: center; }
  .contact__names { font-weight: 700; font-size: 19px; }
  .contact__phone { font-weight: 600; font-size: 14px; margin-top: 2px; }
  .contact__dots { border-top: 2px dotted var(--ink); margin: 14px 0; }
  .contact__line { font-size: 13.5px; line-height: 1.75; color: var(--ink-soft); }

  .front-band { position: absolute; left: 0; bottom: 0; width: 360px; height: 110px; }

  /* back */
  .portrait {
    position: absolute; left: 40px; top: 40px; width: 280px; height: 340px;
    background: radial-gradient(ellipse at 45% 40%, var(--art-mid) 0%, var(--art-dark) 60%, var(--card) 100%);
  }
  .card--back .brand { top: 420px; }
  .card--back .brand__rule { margin-top: 10px; }
  .website { font-size: 14px; letter-spacing: 2px; margin-top: 10px; color: var(--ink); }
</style>
</head>
<body>
<main class="canvas">

  <section class="card card--front">
    <div class="brand">
      <span class="brand__mark"></span>
      <div class="brand__name">Brass and Bristle</div>
      <div class="brand__rule"></div>
      <div class="brand__tagline">Purveyors of gentlemen's waxes, oils and grooming requisites</div>
    </div>

    <div class="contact">
      <div class="contact__names">Tess &amp; Dulcie Abbott</div>
      <div class="contact__phone">M : 0491527306</div>
      <div class="contact__dots"></div>
      <div class="contact__line">tess@brassandbristle.com.au</div>
      <div class="contact__line">dulcie@brassandbristle.com.au</div>
      <div class="contact__dots"></div>
      <div class="contact__line">sales@theboulevardpomade.com.au</div>
      <div class="contact__line">www.brassandbristle.com.au</div>
    </div>

    <svg class="front-band" viewBox="0 0 360 110" aria-hidden="true">
      <rect x="0" y="0" width="360" height="110" fill="var(--band)"/>
      <polygon points="0,0 360,0 360,18 225,18 205,46 155,46 135,18 0,18" fill="var(--card)"/>
      <polyline points="0,26 131,26 151,54 209,54 229,26 360,26" fill="none" stroke="var(--card)" stroke-width="2"/>
    </svg>
  </section>

  <section class="card card--back">
    <div class="portrait" role="img" aria-label="Grey illustration of a moustached gentleman with a pair of open barber's scissors"></div>
    <div class="brand">
      <div class="brand__name">Brass and Bristle</div>
      <div class="brand__rule"></div>
      <div class="brand__tagline">Purveyors of gentlemen's waxes, oils and grooming requisites</div>
      <div class="website">www.brassandbristle.com.au</div>
    </div>
  </section>

</main>
</body>
</html>
```